CPA Firm Business Card
Halvorin, Bestwick & Pardue CPAs, LLC
Project: CPA Firm Business Card
CPA Firm Business Card - Financial Services
Creative Brief
Professional
Moss Brandley, CPA
2867 E. Sable Way, Suite 348 Tucson, AZ 85619
moss@quillledger.net
In addition to business cards design I would also like to see designs for letterheads, envelopes and fax cover sheets.

```html
<!DOCTYPE html>
<html lang="en">
<head>
<meta charset="utf-8">
<title>Halvorin, Bestwick &amp; Pardue CPAs, LLC — Business Card</title>
<link rel="stylesheet" href="https://fonts.googleapis.com/css2?family=Open+Sans:wght@400;600;700;800&display=swap">
<style>
  :root {
    --bg: #2b2b2d;
    --card: #ffffff;
    --wine: #7a1a1f;
    --wine-dark: #5c1115;
    --ink: #555659;
    --ink-soft: #7b7c80;
    --rule: #9a9b9e;
    --silver: #c9cacd;
    --silver-light: #e6e7e9;
  }
  * { margin: 0; padding: 0; box-sizing: border-box; }
  html, body { width: 1200px; height: 901px; overflow: hidden; }
  body {
    background: var(--bg);
    font-family: "Open Sans", Arial, sans-serif;
    position: relative;
  }
  .card {
    position: absolute;
    left: 100px; top: 165px;
    width: 1000px; height: 570px;
    background: var(--card);
    border-radius: 40px;
    overflow: hidden;
  }
  .firm-name {
    position: absolute;
    left: 430px; top: 58px;
    display: flex; align-items: center; gap: 18px;
  }
  .firm-name__square {
    width: 64px; height: 64px;
    background: var(--wine);
    flex: none;
  }
  .firm-name__text {
    color: var(--wine);
    font-weight: 800;
    font-size: 34px;
    line-height: 1.02;
    text-transform: uppercase;
    letter-spacing: 0.5px;
  }
  .firm-name__text small {
    display: block;
    font-size: 18px;
    text-align: right;
    letter-spacing: 1px;
  }
  .person {
    position: absolute;
    left: 92px; top: 248px;
    color: var(--wine);
    font-weight: 600;
    font-size: 29px;
  }
  .divider {
    position: absolute;
    left: 486px; top: 236px;
    width: 2px; height: 190px;
    background: var(--rule);
  }
  .contact {
    position: absolute;
    left: 512px; top: 236px;
    color: var(--ink);
    font-size: 21px;
    line-height: 1.38;
    list-style: none;
  }
  .contact li { display: flex; align-items: center; gap: 10px; }
  .contact .address { display: block; margin-bottom: 14px; }
  .contact svg { width: 18px; height: 18px; flex: none; }
  .swoosh {
    position: absolute;
    left: 0; bottom: 0;
    width: 1000px; height: 190px;
  }
  .website {
    position: absolute;
    left: 70px; bottom: 30px;
    color: #ffffff;
    font-size: 17px;
    letter-spacing: 6px;
    transform: rotate(4deg);
    transform-origin: left bottom;
  }
</style>
</head>
<body>
  <div class="card">
    <div class="firm-name">
      <span class="firm-name__square"></span>
      <span class="firm-name__text">Halvorin<br>Bestwick &amp;<br>Pardue<small>CPAs, LLC</small></span>
    </div>

    <p class="person">Moss Brandley, CPA</p>
    <div class="divider"></div>

    <ul class="contact">
      <li class="address">2867 E. Sable Way, Suite 348<br>Tucson, AZ 85619</li>
      <li>
        <svg viewBox="0 0 24 24" aria-hidden="true"><path fill="#5c1115" d="M6.6 10.8a15 15 0 0 0 6.6 6.6l2.2-2.2c.3-.3.7-.4 1-.2 1.1.4 2.3.6 3.6.6.6 0 1 .4 1 1V20c0 .6-.4 1-1 1A17 17 0 0 1 3 4c0-.6.4-1 1-1h3.5c.6 0 1 .4 1 1 0 1.3.2 2.5.6 3.6.1.3 0 .7-.2 1z"/></svg>
        520-555-0148
      </li>
      <li>
        <svg viewBox="0 0 24 24" aria-hidden="true"><rect x="5" y="3" width="14" height="6" fill="#5c1115"/><rect x="2" y="9" width="20" height="9" rx="2" fill="#5c1115"/><rect x="6" y="14" width="12" height="7" fill="#fff" stroke="#5c1115" stroke-width="2"/></svg>
        520-555-0172
      </li>
      <li>
        <svg viewBox="0 0 24 24" aria-hidden="true"><rect x="2" y="5" width="20" height="14" rx="2" fill="#5c1115"/><path d="M3 6l9 7 9-7" fill="none" stroke="#fff" stroke-width="1.8"/></svg>
        moss@quillledger.net
      </li>
    </ul>

    <svg class="swoosh" viewBox="0 0 1000 190" preserveAspectRatio="none" aria-hidden="true">
      <defs>
        <linearGradient id="silverBand" x1="0" y1="0" x2="0" y2="1">
          <stop offset="0" stop-color="#e6e7e9"/>
          <stop offset="1" stop-color="#a9aaad"/>
        </linearGradient>
        <linearGradient id="wineBand" x1="0" y1="0" x2="0" y2="1">
          <stop offset="0" stop-color="#8a2026"/>
          <stop offset="1" stop-color="#5c1115"/>
        </linearGradient>
      </defs>
      <path d="M0 30 C 280 150, 720 140, 1000 0 L1000 190 L0 190 Z" fill="url(#silverBand)"/>
      <path d="M0 78 C 280 190, 720 180, 1000 60 L1000 190 L0 190 Z" fill="url(#wineBand)"/>
    </svg>
    <span class="website">www.quillledger.net</span>
  </div>
</body>
</html>
```